Rw building ventures pty ltd

This is a development and construction company. Website can be set up on our domain rwbuildworks.net if we could change the domain to rwbuildworks.com.au would be great

Want the page to have eye catching designs, red, black and white are the preffered colours.

Check out www.toluqin.com.au it is my former company with my partner which i am now venturing out on my own, that is the perfect example of the website i want even allot of the information would be the same

Industry/Entity Type

Construction

Coding

Coded - Design and coding required

Number of Pages Required

5+ page

Requirements
Must have
• Company logo eye catching designs

```html
<!DOCTYPE html>
<html lang="en">
<head>
<meta charset="utf-8">
<title>RW Buildworks</title>
<link rel="stylesheet" href="https://fonts.googleapis.com/css2?family=Roboto:wght@400;500;700;900&display=swap">
<style>
:root{
  --red:#ee1c1c;
  --black:#111;
  --dark:#1c1c1c;
  --grey:#ebebeb;
  --white:#fff;
  --text:#333;
}
*{box-sizing:border-box;margin:0;padding:0}
html,body{width:1200px;height:4812px;overflow:hidden}
body{position:relative;font-family:"Roboto",Arial,sans-serif;color:var(--text);background:var(--white)}
.abs{position:absolute}
.btn{position:absolute;display:flex;align-items:center;justify-content:center;background:var(--red);color:var(--white);font-weight:700;text-transform:uppercase}
.brand{position:absolute;font-weight:700;letter-spacing:2px;display:flex;align-items:center;gap:10px}
.brand i{display:block;width:14px;height:14px;background:var(--red)}
.photo{position:absolute}
h2.sec{position:absolute;left:0;width:1200px;text-align:center;font-weight:700;font-size:30px}
h2.sec span{color:var(--red)}
.rule{position:absolute;height:3px;background:var(--red)}

/* header */
.header{position:absolute;left:0;top:0;width:1200px;height:116px;background:var(--white)}
.phone-tab{position:absolute;left:899px;top:0;width:187px;height:37px;background:var(--red);color:var(--white);font-weight:700;font-size:20px;display:flex;align-items:center;justify-content:center;gap:10px}
.nav{position:absolute;left:518px;top:72px;width:568px;display:flex;justify-content:space-between;font-size:15px;font-weight:700;color:var(--black)}
.nav .active{color:var(--red)}
.nav-mark{position:absolute;left:500px;top:110px;width:80px;height:5px;background:var(--red)}

/* hero */
.hero{position:absolute;left:0;top:116px;width:1200px;height:488px;background:linear-gradient(180deg,#4a4d52,#3a3530 60%,#2b2b2b)}
.hero h1{position:absolute;left:0;top:112px;width:1200px;text-align:center;color:var(--white);font-size:52px;font-weight:700}
.hero p{position:absolute;left:300px;top:208px;width:600px;text-align:center;color:var(--white);font-size:19px;line-height:25px}
.hero .outline{position:absolute;left:495px;top:299px;width:208px;height:56px;border:3px solid var(--white);color:var(--white);font-weight:700;font-size:19px;display:flex;align-items:center;justify-content:center}
.arrow{position:absolute;top:219px;width:53px;height:50px;background:rgba(255,255,255,.85);display:flex;align-items:center;justify-content:center}

/* about */
.about h2{position:absolute;left:112px;top:710px;font-size:31px;font-weight:700;color:var(--black)}
.about h2 span{color:var(--red)}
.about p{position:absolute;left:116px;top:804px;width:540px;font-size:14px;line-height:18.5px;color:#222}

/* services */
.services{position:absolute;left:0;top:1196px;width:1200px;height:705px;background:var(--grey)}
.card{position:absolute;top:1396px;width:312px;height:413px;background:var(--white);box-shadow:0 2px 6px rgba(0,0,0,.15)}
.card .photo{left:0;top:0;width:312px;height:195px}
.card h3{position:absolute;left:0;top:224px;width:312px;text-align:center;font-size:20px;font-weight:700;color:var(--black)}
.card p{position:absolute;left:36px;top:266px;width:240px;text-align:center;font-size:13px;line-height:16px}
.card .btn{left:88px;top:333px;width:136px;height:41px;font-size:14px}

/* projects */
.projects{position:absolute;left:0;top:1901px;width:1200px;height:669px;background:linear-gradient(180deg,#2a2a2a,#161616 55%,#0d0d0d)}
.dot{position:absolute;width:18px;height:18px;border-radius:50%}

/* quality */
.quality h2{position:absolute;left:664px;top:2658px;font-size:31px;font-weight:700;color:var(--black);line-height:38px}
.quality h2 span{color:var(--red)}
.quality p{position:absolute;left:671px;width:412px;font-size:14px;line-height:18.5px;color:#222}

/* testimonials */
.testi{position:absolute;left:0;top:3258px;width:1200px;height:458px;background:linear-gradient(180deg,#202020,#141414)}
.tcard{position:absolute;top:3372px;height:222px;background:var(--white);overflow:hidden}
.tcard p{position:absolute;left:38px;top:42px;width:380px;font-size:14px;line-height:17px;color:#222}
.tcard h4{position:absolute;left:38px;top:126px;font-size:19px;color:var(--red);font-weight:700}
.tcard small{position:absolute;left:41px;top:156px;font-size:13px;font-weight:700;color:var(--black)}

/* quote */
.foot-bg{position:absolute;left:0;top:4267px;width:1200px;height:469px;background:var(--black)}
.quote{position:absolute;left:110px;top:3850px;width:978px;height:486px;background:var(--red)}
.quote h2{position:absolute;left:0;top:50px;width:978px;text-align:center;color:var(--white);font-size:34px;font-weight:700}
.field{position:absolute;background:var(--white);color:#777;font-size:15px;font-weight:500;padding:20px 0 0 20px}
.submit{position:absolute;left:406px;top:396px;width:168px;height:53px;background:var(--black);color:var(--white);font-weight:700;font-size:18px;display:flex;align-items:center;justify-content:center}

/* footer */
.footer{color:var(--white)}
.footer h5{position:absolute;font-size:18px;font-weight:700;color:var(--white)}
.footer .link{position:absolute;left:503px;font-size:15px}
.footer .info{position:absolute;left:161px;font-size:15px}
.footer .ico{position:absolute;left:115px}
.bottom{position:absolute;left:0;top:4736px;width:1200px;height:76px;background:var(--red)}
.social{position:absolute;top:4757px;width:32px;height:32px;border-radius:50%;background:var(--white)}
.copy{position:absolute;right:110px;top:4762px;color:var(--white);font-size:16px}
</style>
</head>
<body>

<!-- header -->
<header class="header">
  <div class="brand" style="left:108px;top:36px;font-size:28px;color:var(--black)"><i></i>RW BUILDWORKS</div>
  <div class="phone-tab">
    <svg width="20" height="20" viewBox="0 0 24 24"><path fill="#fff" d="M6.6 10.8a15.1 15.1 0 0 0 6.6 6.6l2.2-2.2a1 1 0 0 1 1-.25 11.4 11.4 0 0 0 3.6.57 1 1 0 0 1 1 1V20a1 1 0 0 1-1 1A17 17 0 0 1 3 4a1 1 0 0 1 1-1h3.5a1 1 0 0 1 1 1c0 1.25.2 2.45.57 3.57a1 1 0 0 1-.25 1z"/></svg>
    555-410 732
  </div>
  <nav class="nav">
    <span class="active">HOME</span><span>ABOUT US</span><span>SERVICES</span><span>PROJECTS</span><span>BLOG</span><span>CONTACT</span>
  </nav>
  <div class="nav-mark"></div>
</header>

<!-- hero -->
<section class="hero" role="img" aria-label="Modern two-storey townhouses with timber battens and dark brick, darkened">
  <h1>CONSTRUCTION</h1>
  <p>Lorem ipsum dolor sit amet, consectetur adipiscing elit, sed do viverra maecenas accumsan lacus vel facilisis.</p>
  <div class="outline">READ MORE</div>
  <div class="arrow" style="left:22px"><svg width="20" height="30" viewBox="0 0 20 30"><path d="M16 3 4 15l12 12" stroke="#111" stroke-width="3" fill="none"/></svg></div>
  <div class="arrow" style="left:1129px"><svg width="20" height="30" viewBox="0 0 20 30"><path d="M4 3l12 12L4 27" stroke="#111" stroke-width="3" fill="none"/></svg></div>
</section>

<!-- about -->
<section class="about">
  <h2>ABOUT <span>OUR COMPANY</span></h2>
  <div class="rule" style="left:112px;top:759px;width:93px"></div>
  <p>Lorem ipsum dolor sit amet, consectetur adipiscing elit. Sed non libero to a us consectetur, blandit mauris eget, imperdiet nisl. Etiam commodo ex nec erat tempor varius. Nunc rutrum pretium nunc in malesuada. Curabitur mollis urna ac sapien vulputate, ut congue sapien vehicula. Cum sociis natoque penatibus et magnis dis parturient montes, nascetur ridiculus mus. Nam et suscipit dui. Maecenas velit quam, mollis id erat eget, scelerisque elementum odio. our to Maecenas ac sagittis erat. Quisque hendrerit dapibus diam, a venenatis dui a efficitur nec. Aenean tincidunt ullamcorper fermentum.</p>
  <div class="btn" style="left:116px;top:991px;width:170px;height:54px;font-size:17px">READ MORE</div>
  <div class="abs" style="left:744px;top:690px;width:336px;height:402px;background:var(--red)"></div>
  <div class="photo" role="img" aria-label="White modern house with dark brick base and a parked car" style="left:736px;top:682px;width:337px;height:402px;background:linear-gradient(180deg,#8fa6bf,#c9d2d8 45%,#e4e4e2 60%,#3a3a3a)"></div>
</section>

<!-- services -->
<section class="services"></section>
<h2 class="sec" style="top:1294px;color:var(--black)">OUR <span>SERVICES</span></h2>
<div class="rule" style="left:553px;top:1350px;width:94px"></div>

<div class="card" style="left:112px">
  <div class="photo" role="img" aria-label="Building site with timber boards and a concrete slab" style="background:linear-gradient(180deg,#9aa3ad,#8f8a80 40%,#6e6359)"></div>
  <h3>CONSTRUCTION</h3>
  <p>Lorem ipsum dolor sit amet, consect etur adipiscing elit, sed do eiusmod t empor incididunt ut labore</p>
  <div class="btn">READ MORE</div>
</div>
<div class="card" style="left:443px">
  <div class="photo" role="img" aria-label="Row of new two-storey townhouses" style="background:linear-gradient(180deg,#a7c4dc,#c4d3de 40%,#5c4d45 70%,#8a8a85)"></div>
  <h3>HOUSE BUILDS</h3>
  <p>Lorem ipsum dolor sit amet, consect etur adipiscing elit, sed do eiusmod t empor incididunt ut labore</p>
  <div class="btn">READ MORE</div>
</div>
<div class="card" style="left:772px">
  <div class="photo" role="img" aria-label="Renovated backyard with a swimming pool" style="background:linear-gradient(180deg,#9fc2de,#e6e8ea 45%,#2f9fb0 70%,#b9b6ae)"></div>
  <h3>RENOVATION</h3>
  <p>Lorem ipsum dolor sit amet, consect etur adipiscing elit, sed do eiusmod t empor incididunt ut labore</p>
  <div class="btn">READ MORE</div>
</div>

<!-- projects -->
<section class="projects" role="img" aria-label="Dark background of builders working on scaffolding"></section>
<h2 class="sec" style="top:2070px;color:var(--white)">OUR PROJECTS</h2>
<div class="rule" style="left:553px;top:2121px;width:94px"></div>
<div class="photo" role="img" aria-label="Stacked timber and steel on site" style="left:0;top:2183px;width:172px;height:193px;background:linear-gradient(135deg,#6e5a48,#a88a6c,#4a4038)"></div>
<div class="photo" role="img" aria-label="Bright open-plan living room" style="left:189px;top:2183px;width:250px;height:193px;background:linear-gradient(180deg,#f2f2f0,#dcd8d2 60%,#a9a29a)"></div>
<div class="photo" role="img" aria-label="Modern grey and white two-storey home" style="left:452px;top:2164px;width:294px;height:228px;background:linear-gradient(180deg,#2f6fc4,#8fb3df 35%,#d9d9d6 55%,#4d4d4d)"></div>
<div class="photo" role="img" aria-label="Contemporary townhouse facade with glass fence" style="left:757px;top:2183px;width:252px;height:193px;background:linear-gradient(180deg,#8aa8c8,#6f7377 45%,#9fc7c8 80%,#4f4f4f)"></div>
<div class="photo" role="img" aria-label="Kitchen with timber cabinets and island" style="left:1024px;top:2183px;width:176px;height:193px;background:linear-gradient(180deg,#ece9e4,#b59b7f 55%,#e0dcd6)"></div>
<div class="dot" style="left:557px;top:2449px;background:var(--red)"></div>
<div class="dot" style="left:591px;top:2449px;background:#8a1010"></div>
<div class="dot" style="left:625px;top:2449px;background:#8a1010"></div>

<!-- quality -->
<section class="quality">
  <div class="abs" style="left:110px;top:2751px;width:344px;height:408px;background:var(--red)"></div>
  <div class="photo" role="img" aria-label="Townhouse exterior with a red car in the driveway" style="left:118px;top:2751px;width:336px;height:402px;background:linear-gradient(180deg,#8fb0cf,#b7b3ac 50%,#5d7a4a 85%,#3d3d3d)"></div>
  <div class="photo" role="img" aria-label="Floating timber staircase with glass balustrade" style="left:235px;top:2665px;width:337px;height:400px;background:linear-gradient(160deg,#d4d4d2,#a9a9a7 55%,#7d6e5b 75%,#9c9c9a)"></div>
  <h2>QUALTIY, INNOVATION<br><span style="margin-left:112px">&amp; EXCELLENCE</span></h2>
  <div class="rule" style="left:669px;top:2712px;width:90px"></div>
  <p style="top:2770px">Our commitment to quality and excellence in home design has helped us become the builders we are today. We've never been satisfied with simply building homes 'the way it's always been done.' This is what sets our company apart from the rest. In fact, our passion for innovation is at the heart of our business our constant search for innovation is always at our core.</p>
  <p style="top:2918px">Our contemporary home designs continually evolve to meet Australia's changing lifestyle demands, and we're constantly inspiring our customers with new creative ideas such as</p>
  <div class="btn" style="left:673px;top:3039px;width:168px;height:54px;font-size:17px">READ MORE</div>
</section>

<!-- testimonials -->
<section class="testi" role="img" aria-label="Dark background of workers on a building frame"></section>
<div class="rule" style="left:150px;top:3398px;width:89px"></div>
<div class="abs" style="left:112px;top:3386px;width:219px;text-align:right;color:var(--white);font-size:30px;font-weight:700;line-height:37px">OUR<br>TESTIMONIALS</div>
<div class="dot" style="left:196px;top:3517px;width:12px;height:12px;background:var(--red)"></div>
<div class="dot" style="left:214px;top:3517px;width:12px;height:12px;background:var(--white)"></div>
<div class="dot" style="left:233px;top:3517px;width:12px;height:12px;background:var(--white)"></div>

<div class="tcard" style="left:402px;width:456px">
  <p>Lorem ipsum dolor sit amet, consectetur adipiscing elit, sed do eiusmod tempor incididunt ut labore et ultrices gravida. Risus commodo viverra maecenas accumsan lacus vel facilisis.</p>
  <h4>Mara</h4>
  <small>Lorem Ipsum</small>
  <div class="abs" style="left:321px;top:99px;width:88px;height:95px;border:3px solid var(--red);padding:5px">
    <div role="img" aria-label="Customer portrait" style="width:100%;height:100%;background:linear-gradient(180deg,#e8e4e0,#8a8580)"></div>
  </div>
</div>
<div class="tcard" style="left:906px;width:294px">
  <p>Lorem ipsum dolor sit amet, consectetur adipiscing elit, sed do eiusmod tempor incididunt ut labore et ultrices gravida. Risus commodo viverra maecenas accumsan lacus vel facilisis.</p>
  <h4>Ellis</h4>
  <small>Lorem Ipsum</small>
</div>

<!-- quote -->
<div class="foot-bg"></div>
<section class="quote">
  <h2>GET A QUOTE</h2>
  <div class="field" style="left:144px;top:113px;width:339px;height:56px">Name :</div>
  <div class="field" style="left:494px;top:113px;width:340px;height:56px">Mobil Number :</div>
  <div class="field" style="left:144px;top:183px;width:339px;height:57px">E mail :</div>
  <div class="field" style="left:494px;top:183px;width:340px;height:57px">Massege :</div>
  <div class="field" style="left:144px;top:253px;width:694px;height:117px">Message</div>
  <div class="submit">SUBMIT</div>
</section>

<!-- footer -->
<footer class="footer">
  <div class="brand" style="left:112px;top:4424px;font-size:28px;color:var(--white)"><i></i>RW BUILDWORKS</div>
  <svg class="ico" style="top:4530px" width="22" height="22" viewBox="0 0 24 24"><path fill="#fff" d="M6.6 10.8a15.1 15.1 0 0 0 6.6 6.6l2.2-2.2a1 1 0 0 1 1-.25 11.4 11.4 0 0 0 3.6.57 1 1 0 0 1 1 1V20a1 1 0 0 1-1 1A17 17 0 0 1 3 4a1 1 0 0 1 1-1h3.5a1 1 0 0 1 1 1c0 1.25.2 2.45.57 3.57a1 1 0 0 1-.25 1z"/></svg>
  <div class="info" style="top:4531px">555 301 4478</div>
  <svg class="ico" style="top:4570px" width="22" height="16" viewBox="0 0 22 16"><rect x="1" y="1" width="20" height="14" fill="none" stroke="#fff" stroke-width="2"/><path d="M1 1l10 8 10-8" fill="none" stroke="#fff" stroke-width="2"/></svg>
  <div class="info" style="top:4568px">info@rwbuildworks.com.au</div>
  <svg class="ico" style="top:4605px" width="20" height="26" viewBox="0 0 20 26"><path fill="#fff" d="M10 0a10 10 0 0 0-10 10c0 7 10 16 10 16s10-9 10-16A10 10 0 0 0 10 0zm0 14a4 4 0 1 1 0-8 4 4 0 0 1 0 8z"/></svg>
  <div class="info" style="top:4608px">Lorem Ipsum,stop to us</div>

  <h5 style="left:499px;top:4397px">COMPANY</h5>
  <div class="link" style="top:4458px">Home</div>
  <div class="link" style="top:4496px">About us</div>
  <div class="link" style="top:4533px">Services</div>
  <div class="link" style="top:4570px">Project</div>
  <div class="link" style="top:4608px">Blog</div>

  <h5 style="left:753px;top:4398px">NEWSLETTER</h5>
  <div class="abs" style="left:755px;top:4455px;width:300px;font-size:15px;line-height:21px">Subscribe to our weekly Newsletter and receive updates via email.</div>
  <div class="abs" style="left:755px;top:4529px;width:275px;height:69px;background:var(--white);color:var(--black);font-size:19px;font-weight:700;padding:22px 0 0 20px">E mail</div>
  <div class="abs" style="left:1030px;top:4529px;width:56px;height:69px;background:var(--red);display:flex;align-items:center;justify-content:center">
    <svg width="34" height="30" viewBox="0 0 24 22"><path fill="#fff" d="M23 1 1 10l7 3 2 7 3-5 6 4z"/></svg>
  </div>
</footer>

<div class="bottom"></div>
<div class="social" style="left:111px"></div>
<div class="social" style="left:160px"></div>
<div class="social" style="left:205px"></div>
<div class="copy">© All Copyright 2021 by Rw building ventures pty ltd</div>

</body>
</html>
```